I need the following on my business card:
- Name: Dana Whitcomb
- License # 0M93216
- Title: Producer
- Phone: (555) 017-3904
- Email: Dana@CorbelInsuranceServices.com

- Company: Corbel Insurance Services
- Address: 27408 Larkmoor Ave Suite 610, Brenton Falls, NV 90217
- Website: www.CorbelInsuranceServices.com

Also add our slogan on the card: "Steady Care For Every Road"

```html
<!DOCTYPE html>
<html lang="en">
<head>
<meta charset="utf-8">
<title>Corbel Insurance Services – Business Card</title>
<link rel="stylesheet" href="https://fonts.googleapis.com/css2?family=Lato:wght@400;700;900&display=swap">
<style>
  :root {
    --navy: #0b2d7d;
    --green: #06993a;
    --ink: #2f2f35;
    --paper: #ffffff;
    --stage: #e9eaec;
    --sky: #d9dde0;
    --snow: #eceef0;
    --field: #c9ab86;
  }
  * { margin: 0; padding: 0; box-sizing: border-box; }
  html, body { width: 1200px; height: 900px; overflow: hidden; }
  body {
    background: var(--stage);
    font-family: "Lato", sans-serif;
    position: relative;
  }
  .card {
    position: absolute;
    left: 250px;
    width: 700px;
    height: 400px;
    background: var(--paper);
    overflow: hidden;
    box-shadow: 0 6px 18px rgba(0,0,0,0.18);
  }
  .card--front { top: 40px; }
  .card--back { top: 460px; }

  /* Front */
  .scenery {
    position: absolute; inset: 0;
    background: linear-gradient(180deg, var(--sky) 0%, var(--snow) 45%, #d8cbb9 70%, var(--field) 100%);
    opacity: 0.85;
  }
  .brand {
    position: absolute; left: 0; right: 0; top: 140px;
    text-align: center;
  }
  .brand__name {
    color: var(--navy);
    font-weight: 900;
    font-size: 40px;
    letter-spacing: 3px;
    text-transform: uppercase;
    line-height: 1;
  }
  .brand__slogan {
    margin-top: 22px;
    color: var(--navy);
    font-weight: 700;
    font-size: 20px;
    letter-spacing: 5px;
  }

  /* Back */
  .corner { position: absolute; }
  .corner--top { left: 0; top: 0; }
  .corner--bottom { right: 0; bottom: 0; }
  .holder {
    position: absolute; right: 42px; top: 100px;
    text-align: right;
  }
  .holder__name {
    color: var(--navy);
    font-weight: 900;
    font-size: 36px;
    letter-spacing: 1px;
    text-transform: uppercase;
    line-height: 1.05;
  }
  .holder__license {
    color: var(--navy);
    font-size: 19px;
    margin-top: 4px;
  }
  .holder__title {
    color: var(--green);
    font-size: 19px;
    margin-top: 4px;
  }
  .contact {
    position: absolute; left: 60px; top: 205px;
    list-style: none;
    color: var(--ink);
    font-size: 17px;
    line-height: 1.45;
  }
  .contact li { display: flex; align-items: flex-start; gap: 10px; }
  .contact svg { flex: none; margin-top: 3px; }
  .contact__company { font-weight: 700; }
</style>
</head>
<body>

<section class="card card--front">
  <div class="scenery" role="img" aria-label="Photograph of snow-capped mountains above a road through golden brush, softly faded"></div>
  <div class="brand">
    <div class="brand__name">Corbel Insurance Services</div>
    <div class="brand__slogan">Steady Care For Every Road</div>
  </div>
</section>

<section class="card card--back">
  <svg class="corner corner--top" width="260" height="130" viewBox="0 0 260 130" aria-hidden="true">
    <polygon points="0,0 260,0 0,130" fill="var(--navy)"/>
  </svg>
  <svg class="corner corner--bottom" width="250" height="160" viewBox="0 0 250 160" aria-hidden="true">
    <polygon points="250,0 250,160 0,160" fill="var(--green)"/>
  </svg>

  <div class="holder">
    <div class="holder__name">Dana Whitcomb</div>
    <div class="holder__license">License # 0M93216</div>
    <div class="holder__title">Producer</div>
  </div>

  <ul class="contact">
    <li>
      <svg width="14" height="18" viewBox="0 0 14 18" aria-hidden="true"><path d="M7 0a7 7 0 0 0-7 7c0 5 7 11 7 11s7-6 7-11a7 7 0 0 0-7-7z" fill="var(--green)"/><circle cx="7" cy="7" r="2.6" fill="#fff"/></svg>
      <span><span class="contact__company">Corbel Insurance Services</span><br>27408 Larkmoor Ave Suite 610<br>Brenton Falls, NV 90217</span>
    </li>
    <li>
      <svg width="14" height="16" viewBox="0 0 24 24" aria-hidden="true"><path d="M6.6 10.8a15 15 0 0 0 6.6 6.6l2.2-2.2a1 1 0 0 1 1-.25 11.4 11.4 0 0 0 3.6.6 1 1 0 0 1 1 1V20a1 1 0 0 1-1 1A17 17 0 0 1 3 4a1 1 0 0 1 1-1h3.5a1 1 0 0 1 1 1c0 1.25.2 2.45.6 3.6a1 1 0 0 1-.25 1z" fill="var(--green)"/></svg>
      <span>(555) 017-3904</span>
    </li>
    <li>
      <svg width="16" height="14" viewBox="0 0 16 12" aria-hidden="true"><rect width="16" height="12" rx="1" fill="var(--green)"/><path d="M1 1l7 5.5L15 1" stroke="#fff" stroke-width="1.4" fill="none"/></svg>
      <span>Dana@CorbelInsuranceServices.com</span>
    </li>
    <li>
      <svg width="16" height="16" viewBox="0 0 16 16" aria-hidden="true"><circle cx="8" cy="8" r="7.5" fill="var(--green)"/><path d="M0.5 8h15M8 0.5c-3 3-3 12 0 15M8 0.5c3 3 3 12 0 15" stroke="#fff" stroke-width="1.1" fill="none"/></svg>
      <span>www.CorbelInsuranceServices.com</span>
    </li>
  </ul>
</section>

</body>
</html>
```